Tea box package for Herbal Teas

We would like a design for a package of our tea products. We want the consumer to understand that our products are natural just by looking at the package. We prefer minimalistic designs.
The package we want would be a square (or slightly rectangular) box. The box would be generic enough for us to use it for different teas. Essentially what we want is all the main information and designs to be the same for each tea product we have. We would like to be able to change the main color and the name of the tea then to customize to the tea in the package. Please see the attached images for examples.
We really like the package in tea_packaging_example_4 picture. We would like our packaging to be something very similar but with all the labels printed on the package.
We already have our logo so I am attaching that as well (image named 'velk ansary logo copy'). That would go on the front of the box.
We also attach a tile created using our logo (see image called 'tile'). We would like this to go to the sides similarly to tea_packaging_example_4.
On the back of the pouch, we want to have directions on how to make the tea but we want this section to be editable. For now just 3-4 lines of sample text is fine along with instructions on how to make a tea, see picture 'back of tea box'.
We would like for the box color to be as in example picture
tea_packaging_example_4. The color of the writing should be the same as the logo color. The font style should be something that would look nice next to the logo font, we are not sure what that font should be. The only thing colored would be the name of the tea and the ribbon as seen in tea_packaging_example_4, which we would like to change if we need to, to other variations.
Thanks a lot. For any questions, please contact me.

```html
<!DOCTYPE html>
<html lang="en">
<head>
<meta charset="utf-8">
<title>Velk Ansary – Herbal Tea Box Dieline</title>
<link rel="stylesheet" href="https://fonts.googleapis.com/css2?family=Crimson+Text:ital,wght@0,400;0,600;0,700;1,400&display=swap">
<style>
  :root{
    --green:#0b6b37;
    --green-edge:#0f7a3a;
    --cream:#f7f2e2;
    --wood-light:#c9a679;
    --wood-mid:#a8835a;
    --wood-dark:#6e4f33;
    --cut:#222;
    --fold:#d22;
    --letterbox:#000;
    --paper:#fff;
  }
  html,body{margin:0;padding:0;overflow:hidden;background:var(--paper);}
  .canvas{width:1200px;height:1200px;position:relative;overflow:hidden;background:var(--paper);}
  .canvas svg{display:block;}
  .serif{font-family:"Crimson Text",Georgia,serif;}
</style>
</head>
<body>
<div class="canvas">
<svg width="1200" height="1200" viewBox="0 0 1200 1200" xmlns="http://www.w3.org/2000/svg" class="serif">
  <defs>
    <linearGradient id="wood" x1="0" y1="0" x2="1" y2="0">
      <stop offset="0" stop-color="var(--wood-mid)"/>
      <stop offset="0.5" stop-color="var(--wood-light)"/>
      <stop offset="1" stop-color="var(--wood-mid)"/>
    </linearGradient>
    <linearGradient id="woodDark" x1="0" y1="0" x2="1" y2="0">
      <stop offset="0" stop-color="var(--wood-dark)"/>
      <stop offset="1" stop-color="#86613f"/>
    </linearGradient>
  </defs>

  <!-- letterbox bands -->
  <rect class="band-top" x="0" y="0" width="1200" height="152" fill="var(--letterbox)"/>
  <rect class="band-bottom" x="0" y="1047" width="1200" height="153" fill="var(--letterbox)"/>

  <!-- glue flap -->
  <path class="glue-flap" d="M24 560 L2 570 L2 840 L24 850 Z" fill="var(--paper)" stroke="var(--cut)" stroke-width="1"/>

  <!-- top dust flaps -->
  <path class="dust-flap-left" d="M322 552 L322 538 L338 520 L346 394 L604 394 L612 400 L612 552 Z" fill="var(--green)" stroke="var(--green-edge)"/>
  <path class="dust-flap-right" d="M902 552 L912 538 L912 394 L1154 394 L1196 530 L1196 552 Z" fill="var(--green)" stroke="var(--green-edge)"/>

  <!-- bottom flaps -->
  <path class="bottom-flap-back" d="M24 858 L322 858 L252 1000 L252 1040 L246 1046 L106 1046 L100 1040 L100 1000 Z" fill="var(--green)" stroke="var(--green-edge)"/>
  <path class="bottom-flap-side" d="M322 858 L612 858 L612 870 L470 920 L470 1000 L462 1008 L330 1008 L322 1000 Z" fill="var(--green)" stroke="var(--green-edge)"/>
  <path class="bottom-flap-front" d="M612 858 L902 858 L902 1046 L836 1046 L828 1038 L828 1000 L684 1000 L684 1038 L676 1046 L612 1046 Z" fill="var(--green)" stroke="var(--green-edge)"/>
  <path class="bottom-flap-side-right" d="M902 858 L1196 858 L1196 1000 L1188 1008 L1056 1008 L1048 1000 L1048 930 L902 870 Z" fill="var(--green)" stroke="var(--green-edge)"/>

  <!-- top lid -->
  <g class="lid">
    <path d="M612 552 L612 248 L622 236 L892 236 L902 248 L902 552 Z" fill="url(#wood)" stroke="var(--green-edge)" stroke-width="2"/>
    <rect x="680" y="236" width="154" height="316" fill="var(--green)"/>
    <rect x="684" y="262" width="146" height="280" fill="#4f9a6c" role="img" aria-label="Cream floral tile pattern on green"/>
    <rect x="688" y="258" width="138" height="22" fill="#3f8d5f" role="img" aria-label="Leaf garland ornament"/>
    <rect x="710" y="370" width="94" height="92" fill="var(--green)" stroke="var(--cream)" stroke-width="2"/>
    <circle cx="757" cy="404" r="13" fill="none" stroke="var(--cream)" stroke-width="2"/>
    <text x="757" y="448" text-anchor="middle" font-size="10" fill="var(--cream)">VELK ANSARY</text>
  </g>

  <!-- back panel -->
  <g class="panel-back">
    <rect x="24" y="552" width="298" height="306" fill="url(#wood)" role="img" aria-label="Light wooden plank texture"/>
    <rect x="294" y="552" width="28" height="306" fill="url(#woodDark)"/>
    <rect x="126" y="552" width="90" height="80" fill="var(--green)"/>
    <circle cx="171" cy="585" r="13" fill="none" stroke="var(--cream)" stroke-width="2"/>
    <text x="171" y="624" text-anchor="middle" font-size="9" fill="var(--cream)">VELK ANSARY</text>
    <rect x="94" y="640" width="158" height="210" fill="var(--green)"/>
    <g class="back-copy" fill="var(--cream)" font-size="7.4" font-style="italic">
      <rect x="96" y="642" width="68" height="10" fill="var(--cream)"/>
      <text x="98" y="650" font-size="8" font-weight="700" font-style="normal" fill="var(--green)">LOREM IPSUM</text>
      <text x="96" y="661">Lorem ipsum dolor sit amet, consectetur</text>
      <text x="96" y="669">adipiscing elit, sed do eiusmod tempor</text>
      <text x="96" y="677">incididunt ut labore et dolore magna aliqua.</text>
      <text x="96" y="685">Ut enim ad minim veniam, quis nostrud</text>
      <text x="96" y="693">exercitation ullamco laboris nisi ut aliquip</text>
      <text x="96" y="701">ex ea commodo consequat. Duis aute irure</text>
      <text x="96" y="709">dolor in reprehenderit in voluptate velit esse</text>
      <text x="96" y="717">cillum dolore eu fugiat nulla pariatur.</text>
      <rect x="96" y="716" width="106" height="10" fill="var(--cream)"/>
      <text x="98" y="724" font-size="8" font-weight="700" font-style="normal" fill="var(--green)">LOREM IPSUM DOLOR:</text>
      <text x="96" y="735" font-style="normal">Lorem ipsum dolor sit amet, consectetur</text>
      <text x="96" y="743" font-style="normal">adipiscing elit, sed do eiusmod tempor</text>
      <text x="96" y="751" font-style="normal">incididunt ut labore et dolore magna aliqua.</text>
    </g>
    <g class="brew-icons" fill="none" stroke="var(--cream)" stroke-width="1.4">
      <rect x="108" y="758" width="18" height="26" rx="2"/>
      <path d="M148 784 h28 M152 784 q-6 -16 10 -20 q16 4 10 20 M176 772 l8 -6"/>
      <circle cx="162" cy="762" r="2"/>
      <circle cx="224" cy="772" r="14"/>
      <path d="M224 763 v9 l6 4"/>
    </g>
    <g fill="var(--cream)" font-size="7" text-anchor="middle">
      <text x="120" y="808">1 sachet</text><text x="120" y="815">per person</text>
      <text x="171" y="808">water</text><text x="171" y="815">80°C</text>
      <text x="223" y="808">brew</text><text x="223" y="815">3-5 minutes</text>
      <text x="230" y="831" font-weight="700" font-size="8">net wt</text>
      <text x="234" y="840" font-size="8">37.5g</text>
    </g>
  </g>

  <!-- left side panel -->
  <g class="panel-side">
    <rect x="322" y="552" width="290" height="306" fill="url(#wood)" role="img" aria-label="Wooden plank texture"/>
    <rect x="322" y="552" width="26" height="306" fill="url(#woodDark)"/>
    <rect x="392" y="552" width="152" height="306" fill="#4f9a6c" role="img" aria-label="Cream floral tile pattern on green"/>
  </g>

  <!-- front panel -->
  <g class="panel-front">
    <rect x="612" y="552" width="290" height="306" fill="url(#wood)" role="img" aria-label="Wooden plank texture"/>
    <rect x="876" y="552" width="26" height="306" fill="url(#woodDark)"/>
    <rect x="680" y="552" width="154" height="306" fill="var(--cream)"/>
    <rect x="684" y="542" width="146" height="22" fill="#7fb393" role="img" aria-label="Leaf garland ornament"/>
    <rect x="712" y="560" width="90" height="80" fill="var(--green)"/>
    <circle cx="757" cy="592" r="14" fill="none" stroke="var(--cream)" stroke-width="2"/>
    <text x="757" y="634" text-anchor="middle" font-size="9" fill="var(--cream)">VELK ANSARY</text>
    <text class="tea-name" x="757" y="682" text-anchor="middle" font-size="38" font-weight="700" fill="var(--green)">LOREM</text>
    <text x="757" y="709" text-anchor="middle" font-size="22" font-weight="700" fill="var(--green)">IPSUM</text>
    <text x="757" y="726" text-anchor="middle" font-size="10.5" letter-spacing="1.2" fill="var(--green)">LOREM IPSUM DOLOR</text>
    <rect class="ribbon" x="687" y="734" width="140" height="98" fill="var(--green)"/>
    <text x="757" y="762" text-anchor="middle" font-size="21" font-weight="700" fill="var(--cream)">HEALTH</text>
    <text x="757" y="777" text-anchor="middle" font-size="12" letter-spacing="1.4" fill="var(--cream)">LOREM IPSUM</text>
    <g fill="var(--cream)" font-size="10.5">
      <text x="700" y="794">Lorem ipsum dolor sit</text>
      <text x="700" y="807">amet, consectetur</text>
      <text x="700" y="820">adipiscing elit</text>
      <text x="816" y="818" text-anchor="end" font-size="8" font-weight="700">net wt</text>
      <text x="814" y="827" text-anchor="end" font-size="8">37.5g</text>
    </g>
    <rect x="680" y="834" width="154" height="24" fill="#7fb393" role="img" aria-label="Leaf garland ornament"/>
  </g>

  <!-- right side panel -->
  <g class="panel-side">
    <rect x="902" y="552" width="294" height="306" fill="url(#wood)" role="img" aria-label="Wooden plank texture"/>
    <rect x="902" y="552" width="26" height="306" fill="url(#woodDark)"/>
    <rect x="974" y="552" width="154" height="306" fill="#4f9a6c" role="img" aria-label="Cream floral tile pattern on green"/>
  </g>

  <!-- fold lines -->
  <g class="folds" stroke="var(--fold)" stroke-width="0.8" fill="none">
    <line x1="24" y1="560" x2="1196" y2="560"/>
    <line x1="24" y1="850" x2="1196" y2="850"/>
    <line x1="322" y1="552" x2="322" y2="858"/>
    <line x1="612" y1="552" x2="612" y2="858"/>
    <line x1="902" y1="552" x2="902" y2="858"/>
    <line x1="636" y1="272" x2="878" y2="272"/>
  </g>
</svg>
</div>
</body>
</html>
```